Website design for an Italian restaurant in Amsterdam

I need a design for a client of mine. It is for Teatro Lucerna, an Italian restaurant in Amsterdam.
We are going for a clean, modern look but we also need to realise an authentic feel.
The restaurant is located in an old movie theatre, that is where the name Teatro Lucerna comes from.
Industry/Entity Type
Italian Restaurant
Number of Pages Required
1 page
Font styles to use
Sans Serif
Colors
Designer to choose colors to be used in the design.

```html
<!DOCTYPE html>
<html lang="en">
<head>
<meta charset="utf-8">
<title>Teatro Lucerna – Ristorante Italiano</title>
<link rel="stylesheet" href="https://fonts.googleapis.com/css2?family=Kreon:wght@400;500&family=Montserrat:wght@600;700&family=Open+Sans:wght@400;600&display=swap">
<style>
:root{
  --ink:#1f1e1e;
  --ink-soft:#2a2828;
  --paper:#ffffff;
  --paper-grey:#f3f3f3;
  --accent:#a8485a;
  --text-dark:#2b2b2b;
  --text-light:#ffffff;
  --muted:#c9c9c9;
  --line:#8a8a8a;
}
*{box-sizing:border-box;margin:0;padding:0}
html,body{width:1200px;height:3523px;overflow:hidden}
body{position:relative;background:var(--paper);font-family:"Open Sans",sans-serif;color:var(--text-dark)}
h1,h2,h3{font-weight:400}
.abs{position:absolute}

/* hero */
.hero{left:0;top:0;width:1200px;height:660px;background:radial-gradient(ellipse at 50% 40%,#2f2d2d,var(--ink) 70%)}
.brand{left:129px;top:26px;display:flex;align-items:center;gap:10px}
.brand-dot{width:28px;height:28px;border-radius:50%;background:var(--accent)}
.brand-name{font-family:"Kreon",serif;font-weight:400;font-size:18px;letter-spacing:.5px;color:var(--text-light);text-transform:uppercase;line-height:1;white-space:nowrap}
.brand-tag{font-family:"Kreon",serif;font-size:10px;color:var(--muted);margin-top:3px}
.nav{left:390px;top:30px;display:flex;gap:2px}
.nav a{font-family:"Kreon",serif;font-weight:400;font-size:13.5px;color:var(--text-light);text-decoration:none;padding:3px 11px;text-transform:uppercase;letter-spacing:.3px;white-space:nowrap}
.nav a.active{background:var(--paper);color:var(--text-dark)}
.call{left:870px;top:31px;display:flex;align-items:center;gap:8px;color:var(--text-light);font-family:"Montserrat",sans-serif;font-weight:600;font-size:14.5px;white-space:nowrap}
.call span{font-weight:400;font-family:"Open Sans",sans-serif;font-size:13.5px}
.hero-title{left:0;width:1200px;top:118px;text-align:center;font-family:"Kreon",serif;font-size:38px;color:var(--text-light)}
.hero-title::before,.hero-title::after{content:"";display:inline-block;width:28px;height:2px;background:var(--text-light);vertical-align:middle;margin:0 22px}
.hero-sub{left:0;width:1200px;top:170px;text-align:center;font-size:12.5px;color:var(--muted)}
.plate{left:350px;top:222px;width:500px;height:500px;border-radius:50%;background:radial-gradient(circle,#f1d28f 0%,#e7bb6d 45%,#d9a45a 58%,#eeeeee 62%,#fafafa 74%,#dcdcdc 100%);box-shadow:0 10px 30px rgba(0,0,0,.35);z-index:2}
.arrow{width:50px;height:50px;border:1.5px solid #6b6b6b;border-radius:50%;top:442px}
.arrow svg{width:100%;height:100%}

/* about */
.about-kicker{left:130px;top:818px;font-family:"Kreon",serif;font-size:26px;color:#555}
.about-title{left:130px;top:852px;font-family:"Kreon",serif;font-size:36px;color:var(--text-dark)}
.about-text{left:134px;top:930px;width:400px;font-size:13px;line-height:22px;color:#333}
.btn{left:134px;top:1087px;width:216px;height:45px;background:var(--accent);color:var(--text-light);font-family:"Montserrat",sans-serif;font-weight:700;font-size:15px;letter-spacing:.5px;display:flex;align-items:center;justify-content:center;text-transform:uppercase}
.photo-room{left:688px;top:810px;width:380px;height:270px;background:linear-gradient(160deg,#3a1412,#6b2a1e 45%,#1c0c0a)}
.photo-tank{left:735px;top:1026px;width:289px;height:176px;border:6px solid var(--paper);background:radial-gradient(ellipse at 50% 50%,#4a7dff,#1834b8 60%,#0a1460)}

/* menu */
.menu{left:0;top:1296px;width:1200px;height:777px;background:var(--ink)}
.section-title{left:0;width:1200px;top:1355px;text-align:center;font-family:"Montserrat",sans-serif;font-weight:700;font-size:22px;color:var(--text-light);letter-spacing:1px}
.section-rule{left:575px;top:1392px;width:50px;height:3px;background:#555}
.menu-col{width:432px}
.menu-col h3{font-family:"Montserrat",sans-serif;font-weight:700;font-size:22px;color:var(--text-light);margin-bottom:22px}
.cat{display:flex;justify-content:space-between;align-items:center;border-bottom:1px solid var(--line);padding:0 4px 6px 4px;font-family:"Montserrat",sans-serif;font-weight:700;font-size:11px;color:var(--text-light);text-transform:uppercase;margin-bottom:22px}
.cat svg{width:12px;height:8px}
.dishes{display:grid;grid-template-columns:152px 82px 150px 48px;row-gap:3px;font-size:11px;line-height:17.5px;color:#dcdcdc;padding:0 4px;margin:-4px 0 32px;white-space:nowrap}

/* gallery */
.gallery-title{left:0;width:1200px;top:2178px;text-align:center;font-family:"Kreon",serif;font-size:36px;color:var(--text-dark)}
.gallery-title::before,.gallery-title::after{content:"";display:inline-block;width:26px;height:2px;background:var(--text-dark);vertical-align:middle;margin:0 20px}
.gallery{left:131px;top:2306px;display:grid;grid-template-columns:repeat(5,167px);grid-auto-rows:160px;column-gap:25px;row-gap:23px}
.tile{width:167px;height:160px}

/* reservation */
.reserve{left:0;top:2766px;width:1200px;height:423px;background:linear-gradient(180deg,#3b2a20,#5a4333 50%,#2a1f18)}
.reserve-title{left:0;width:1200px;top:2850px;text-align:center;font-family:"Kreon",serif;font-size:36px;color:var(--text-light)}
.field{width:218px;height:38px;border:2px solid var(--paper);color:var(--text-light);font-family:"Montserrat",sans-serif;font-weight:700;font-size:11px;padding-left:14px;display:flex;align-items:center;text-transform:uppercase}
.send{width:221px;height:38px;background:var(--accent);color:var(--text-light);font-family:"Montserrat",sans-serif;font-weight:700;font-size:18px;display:flex;align-items:center;justify-content:center}

/* footer */
.footer{left:0;top:3189px;width:1200px;height:334px;background:var(--ink)}
.foot-brand{left:0;width:1200px;top:3252px;display:flex;flex-direction:column;align-items:center}
.follow{left:0;width:1200px;top:3330px;display:flex;justify-content:center;align-items:center;gap:10px;font-family:"Kreon",serif;font-size:15px;color:var(--text-light)}
.social{width:28px;height:28px;border-radius:50%;background:#3a5ab8}
.foot-links{left:0;width:1200px;top:3390px;text-align:center;font-family:"Kreon",serif;font-size:13px;color:var(--text-light);word-spacing:2px}
.copyright{left:0;width:1200px;top:3440px;text-align:center;font-family:"Kreon",serif;font-size:13px;color:var(--text-light)}
</style>
</head>
<body>

<section class="abs hero"></section>
<svg class="abs" style="left:0;top:620px;z-index:1" width="1200" height="50" viewBox="0 0 1200 50">
  <path d="M0 22 L40 26 L90 18 L140 28 L200 20 L260 27 L320 17 L380 25 L440 21 L500 29 L560 18 L620 26 L680 19 L740 27 L800 20 L860 28 L920 18 L980 26 L1040 21 L1100 28 L1160 19 L1200 24 L1200 50 L0 50 Z" fill="var(--paper)"/>
</svg>

<header>
  <div class="abs brand">
    <div class="brand-dot"></div>
    <div><div class="brand-name">Teatro Lucerna</div><div class="brand-tag">Ristorante Italiano</div></div>
  </div>
  <nav class="abs nav">
    <a class="active">Home</a><a>Menu</a><a>Groupmenu</a><a>Reservation</a><a>Contact</a>
  </nav>
  <div class="abs call">
    <svg width="16" height="16" viewBox="0 0 24 24"><path d="M6.6 10.8a15 15 0 0 0 6.6 6.6l2.2-2.2c.3-.3.7-.4 1-.2 1.1.4 2.3.6 3.6.6.6 0 1 .4 1 1V20c0 .6-.4 1-1 1A17 17 0 0 1 3 4c0-.6.4-1 1-1h3.5c.6 0 1 .4 1 1 0 1.3.2 2.5.6 3.6.1.3 0 .7-.2 1z" fill="#fff"/></svg>
    <span>Call :</span> (+31) 20 555 0182
  </div>
</header>

<h1 class="abs hero-title">Italian Food</h1>
<p class="abs hero-sub">Lorem Ipsum is simply dummy text of the printing typesetting</p>
<div class="abs plate" role="img" aria-label="Plate of spaghetti with prawns and basil, seen from above"></div>
<div class="abs arrow" style="left:215px"><svg viewBox="0 0 50 50"><path d="M28 17 L20 25 L28 33" stroke="#777" stroke-width="2" fill="none"/></svg></div>
<div class="abs arrow" style="left:925px"><svg viewBox="0 0 50 50"><path d="M22 17 L30 25 L22 33" stroke="#777" stroke-width="2" fill="none"/></svg></div>

<section>
  <h2 class="abs about-kicker">About</h2>
  <h2 class="abs about-title">Teatro Lucerna</h2>
  <p class="abs about-text">There are many variations of passages of Lorem Ipsum available, but the majority have suffered alteration in some form, by injected humour, or randomised words which don't look even slightly believable. If you are going to use a passage of Lorem Ipsum, you need to be .</p>
  <div class="abs btn">Reserve a table</div>
  <div class="abs photo-room" role="img" aria-label="Dining room of the restaurant in warm red light"></div>
  <div class="abs photo-tank" role="img" aria-label="Large blue-lit aquarium in the restaurant"></div>
</section>

<section class="abs menu"></section>
<svg class="abs" style="left:0;top:1280px" width="1200" height="30" viewBox="0 0 1200 30">
  <path d="M0 14 L60 10 L120 18 L180 9 L240 16 L300 11 L360 19 L420 10 L480 15 L540 8 L600 17 L660 11 L720 18 L780 9 L840 16 L900 10 L960 18 L1020 11 L1080 17 L1140 9 L1200 15 L1200 30 L0 30 Z" fill="var(--ink)"/>
</svg>
<svg class="abs" style="left:0;top:2060px" width="1200" height="30" viewBox="0 0 1200 30">
  <path d="M0 0 L1200 0 L1200 14 L1140 20 L1080 12 L1020 21 L960 13 L900 19 L840 11 L780 20 L720 12 L660 18 L600 10 L540 19 L480 13 L420 21 L360 12 L300 18 L240 11 L180 20 L120 12 L60 19 L0 13 Z" fill="var(--ink)"/>
</svg>
<h2 class="abs section-title">OUR MENU</h2>
<div class="abs section-rule"></div>

<div class="abs menu-col" style="left:131px;top:1475px">
  <h3>LUNCH</h3>
  <div class="cat">Antipasti <svg viewBox="0 0 12 8"><path d="M1 7 L6 2 L11 7" stroke="#aaa" fill="none"/></svg></div>
  <div class="dishes">
    <span>Pane Burro e Tapanada</span><span>€ 4,50</span><span>Pomodorini</span><span>€ 13,50</span>
    <span>Carpaccio di Manzo</span><span>€ 13,50</span><span>Melanzana alla Parmigiana</span><span>€ 11,50</span>
    <span>Carpaccio di Tonno</span><span>€ 14,50</span><span>Sauté di Cozze e Vongole</span><span>€ 15,50</span>
    <span>Vitello Tonnato</span><span>€ 14,75</span><span>Gamberi al Forno</span><span>€ 12,50</span>
    <span>Antipasto Italiano</span><span>€ 16,00 p.p.</span><span>Frittura di Calamari ...</span><span>€ 13,50</span>
    <span>Basilico</span><span>€ 6,50</span><span></span><span></span>
    <span>Mozzarella</span><span>€ 4,50</span><span></span><span></span>
  </div>
  <div class="cat">Salads <svg viewBox="0 0 12 8"><path d="M1 1 L6 6 L11 1" stroke="#aaa" fill="none"/></svg></div>
  <div class="cat">The Pasta <svg viewBox="0 0 12 8"><path d="M1 1 L6 6 L11 1" stroke="#aaa" fill="none"/></svg></div>
  <div class="cat">The Fish <svg viewBox="0 0 12 8"><path d="M1 1 L6 6 L11 1" stroke="#aaa" fill="none"/></svg></div>
  <div class="cat">Meat <svg viewBox="0 0 12 8"><path d="M1 1 L6 6 L11 1" stroke="#aaa" fill="none"/></svg></div>
  <div class="cat">Side Dishes <svg viewBox="0 0 12 8"><path d="M1 1 L6 6 L11 1" stroke="#aaa" fill="none"/></svg></div>
  <div class="cat">Sweet <svg viewBox="0 0 12 8"><path d="M1 1 L6 6 L11 1" stroke="#aaa" fill="none"/></svg></div>
</div>

<div class="abs menu-col" style="left:636px;top:1475px">
  <h3>WIJNEN</h3>
  <div class="cat">Rode Wijnen <svg viewBox="0 0 12 8"><path d="M1 1 L6 6 L11 1" stroke="#aaa" fill="none"/></svg></div>
  <div class="cat">Witte Wijnen <svg viewBox="0 0 12 8"><path d="M1 1 L6 6 L11 1" stroke="#aaa" fill="none"/></svg></div>
</div>

<section>
  <h2 class="abs gallery-title">Photo Gallery</h2>
  <div class="abs gallery">
    <div class="tile" role="img" aria-label="Sandwiches on a plate" style="background:linear-gradient(135deg,#6a5238,#c49a62)"></div>
    <div class="tile" role="img" aria-label="Grilled steak with potatoes" style="background:linear-gradient(135deg,#e8e6e3,#7a3b20)"></div>
    <div class="tile" role="img" aria-label="Salmon with green asparagus" style="background:linear-gradient(135deg,#6c8a3c,#e0835a)"></div>
    <div class="tile" role="img" aria-label="Noodle dish in a dark bowl" style="background:linear-gradient(135deg,#3a3633,#b0653a)"></div>
    <div class="tile" role="img" aria-label="Raw salmon fillet with herbs" style="background:linear-gradient(135deg,#4a3a33,#e2694a)"></div>
    <div class="tile" role="img" aria-label="Burger with fries" style="background:linear-gradient(135deg,#2e2a28,#c98a3a)"></div>
    <div class="tile" role="img" aria-label="Stack of pancakes with banana" style="background:linear-gradient(135deg,#d9d2c8,#c06a2a)"></div>
    <div class="tile" role="img" aria-label="Pasta salad in a bowl" style="background:linear-gradient(135deg,#1e1e1e,#a3823c)"></div>
    <div class="tile" role="img" aria-label="Table with assorted small dishes" style="background:linear-gradient(135deg,#d8c7b0,#b8532e)"></div>
    <div class="tile" role="img" aria-label="Shared plates of salads and dips" style="background:linear-gradient(135deg,#232a22,#8a4a3a)"></div>
  </div>
</section>

<section class="abs reserve" role="img" aria-label="Restaurant interior with tables and chairs, darkened"></section>
<h2 class="abs reserve-title">Reservation</h2>
<div class="abs field" style="left:247px;top:2954px">Name</div>
<div class="abs field" style="left:488px;top:2954px">E mail</div>
<div class="abs field" style="left:728px;top:2954px">Phone</div>
<div class="abs field" style="left:247px;top:3020px">When</div>
<div class="abs field" style="left:488px;top:3020px">Guests</div>
<div class="abs send" style="left:728px;top:3020px">SEND</div>

<footer class="abs footer"></footer>
<div class="abs foot-brand">
  <div style="display:flex;align-items:center;gap:10px">
    <div class="brand-dot" style="width:24px;height:24px"></div>
    <div class="brand-name">Teatro Lucerna</div>
  </div>
  <div class="brand-tag" style="margin-top:6px">Ristorante Italiano</div>
</div>
<div class="abs follow">Follow us : <span class="social"></span><span class="social"></span></div>
<p class="abs foot-links">Home &nbsp;| &nbsp; Menu (new) &nbsp;| &nbsp;Groupmenu &nbsp;| &nbsp;Reservation &nbsp;| &nbsp;Contact</p>
<p class="abs copyright">Copyrights @ 2018 All Rights Reserved</p>

</body>
</html>
```